Velvet Pressings Techno Label Business Card

I'm looking for a very clean business card for my Velvet Pressings music label. The label focusses on techno music. The card should include:

• my name : Daniel Hovind as "Founder & CEO"
• email address: daniel@velvet-pressings.net
• web: www.velvet-pressings.net
• facebook logo + /velvetprs
• twitter logo + /velvetprs
• soundcloud logo + /velvetpressings

Feel free to include your ideas! I'm looking forward to discuss about it.

Daniel

Industry/Entity Type

Business

Contact Information for Business Card

I don't like glossy cards. Prefer matt.

Requirements
Nice to have
• Maybe on one side the complete logo, other side just the icon.
Should not have
• Flashy stuff. Must be clean and business like style.

```html
<!DOCTYPE html>
<html lang="en">
<head>
<meta charset="utf-8">
<title>Velvet Pressings – Business Card</title>
<link href="https://fonts.googleapis.com/css2?family=Source+Sans+3:wght@400;700&display=swap" rel="stylesheet">
<style>
  :root {
    --stage: #3b3b3a;
    --accent: #ff6305;
    --accent-faint: rgba(255, 110, 40, 0.10);
    --ink: #5c5c5c;
    --back-dark: #6c6c6c;
    --back-light: #8a8a8a;
    --back-mark: #d2d2d2;
    --front-light: #ffffff;
    --front-dark: #d9d9d9;
  }
  * { margin: 0; padding: 0; box-sizing: border-box; }
  html, body {
    width: 986px; height: 1200px; overflow: hidden;
    background: var(--stage);
    font-family: "Source Sans 3", "Myriad Pro", sans-serif;
  }
  .card {
    position: absolute;
    width: 758px; height: 437px;
    overflow: hidden;
  }
  .card--back {
    left: 108px; top: 137px;
    background: linear-gradient(90deg, var(--back-dark), var(--back-light));
  }
  .card--front {
    left: 103px; top: 642px;
    background: linear-gradient(90deg, var(--front-light) 10%, var(--front-dark));
  }
  .backdrop-disc {
    position: absolute; border-radius: 50%;
  }
  .card--back .backdrop-disc {
    left: -17px; top: -84px; width: 476px; height: 476px;
    background: rgba(255, 255, 255, 0.07);
  }
  .card--front .backdrop-disc {
    left: 291px; top: 127px; width: 484px; height: 484px;
    background: var(--accent-faint);
  }
  .brand {
    position: absolute;
    display: flex; align-items: center; gap: 14px;
    font-weight: 700; letter-spacing: -0.3px; white-space: nowrap;
  }
  .brand__dot { border-radius: 50%; flex: none; }
  .card--back .brand { left: 385px; top: 346px; font-size: 30px; color: var(--back-mark); }
  .card--back .brand__dot { width: 56px; height: 56px; background: var(--back-mark); }
  .card--front .brand { left: 30px; top: 40px; font-size: 28px; color: var(--accent); }
  .card--front .brand__dot { width: 60px; height: 60px; background: var(--accent); }
  .person__name {
    position: absolute; left: 30px; top: 125px;
    font-size: 33px; font-weight: 400; color: var(--accent);
  }
  .person__role {
    position: absolute; left: 30px; top: 165px;
    font-size: 26px; color: var(--ink);
  }
  .contacts {
    position: absolute; left: 30px; top: 215px; list-style: none;
  }
  .contacts li {
    display: flex; align-items: center; height: 35.6px;
    font-size: 26px; color: var(--ink);
  }
  .contacts .icon {
    width: 22px; height: 22px; margin-right: 15px; flex: none;
    display: flex; align-items: center; justify-content: center;
    color: var(--accent); font-weight: 700; font-size: 20px;
  }
  .icon--square::before {
    content: ""; width: 14px; height: 14px; background: var(--accent); display: block;
  }
  .card__band {
    position: absolute; left: 0; bottom: 0; width: 100%; height: 27px;
    background: var(--accent);
  }
</style>
</head>
<body>

<section class="card card--back" aria-label="Card back">
  <div class="backdrop-disc"></div>
  <div class="brand"><span class="brand__dot"></span>Velvet Pressings</div>
</section>

<section class="card card--front" aria-label="Card front">
  <div class="backdrop-disc"></div>
  <div class="brand"><span class="brand__dot"></span>Velvet Pressings</div>
  <h1 class="person__name">Daniel Hovind</h1>
  <p class="person__role">Founder &amp; CEO</p>
  <ul class="contacts">
    <li><span class="icon">@</span>daniel@velvet-pressings.net</li>
    <li><span class="icon">
      <svg width="20" height="20" viewBox="0 0 20 20" fill="none" stroke="#ff6305" stroke-width="1.5">
        <circle cx="10" cy="10" r="8.5"/>
        <ellipse cx="10" cy="10" rx="4" ry="8.5"/>
        <line x1="1.5" y1="10" x2="18.5" y2="10"/>
        <line x1="3" y1="5.5" x2="17" y2="5.5"/>
        <line x1="3" y1="14.5" x2="17" y2="14.5"/>
      </svg></span>www.velvet-pressings.net</li>
    <li><span class="icon icon--square"></span>/velvetprs</li>
    <li><span class="icon icon--square"></span>/velvetprs</li>
    <li><span class="icon icon--square"></span>/velvetpressings</li>
  </ul>
  <div class="card__band"></div>
</section>

</body>
</html>
```